Vellorin - Business Cards for a new venture

create business card for a startup classified business dealing in construction materials, the cards need to have a professional look but modern, more serious than playful, one of the samples must include the official font (attached), please explore using the official colors in the company's logo

Target Market(s)

Energy sector

Contact Information for Business Card

Font styles to use
Other font styles liked:
• suissnord

Requirements
Must have
• corporate colors (in logo attached)
Nice to have
• Official font (in one of the samples) font is : suissnord
Should not have
• Cartoonish look

```html
<!DOCTYPE html>
<html lang="en">
<head>
<meta charset="utf-8">
<title>Vellorin Business Cards</title>
<link href="https://fonts.googleapis.com/css2?family=Orbitron:wght@500;700&display=swap" rel="stylesheet">
<style>
  :root {
    --bg: #a3a3a3;
    --brand-blue: #0f4a7e;
    --card-white: #f7f7f7;
    --ink: #2b2b2b;
    --muted: #8a8a8a;
    --rule: #9c9c9c;
    --on-blue: #ffffff;
  }
  * { margin: 0; padding: 0; box-sizing: border-box; }
  html, body { width: 1200px; height: 900px; overflow: hidden; }
  body {
    background: var(--bg);
    font-family: "Orbitron", sans-serif;
    display: flex;
    flex-direction: column;
    align-items: center;
    justify-content: center;
    gap: 56px;
  }
  .card {
    width: 620px;
    height: 354px;
    border-radius: 22px;
    position: relative;
    overflow: hidden;
  }
  .card-front {
    background: var(--brand-blue);
    display: flex;
    align-items: center;
    justify-content: center;
  }
  .front-wordmark {
    color: var(--on-blue);
    font-weight: 500;
    font-size: 34px;
    letter-spacing: 6px;
  }
  .card-back { background: var(--card-white); }
  .back-wordmark {
    position: absolute;
    top: 70px;
    left: 330px;
    width: 230px;
    text-align: center;
    color: var(--muted);
    font-weight: 500;
    font-size: 24px;
    letter-spacing: 4px;
  }
  .divider {
    position: absolute;
    top: 138px;
    left: 40px;
    width: 540px;
    height: 1px;
    background: var(--rule);
  }
  .holder { position: absolute; top: 160px; left: 40px; }
  .holder-name {
    color: var(--brand-blue);
    font-weight: 700;
    font-size: 27px;
  }
  .holder-title {
    color: var(--ink);
    font-weight: 500;
    font-size: 15px;
    margin-top: 4px;
    padding-bottom: 10px;
    border-bottom: 1px solid var(--rule);
    width: 190px;
  }
  .contact-list {
    list-style: none;
    position: absolute;
    top: 240px;
    left: 40px;
  }
  .contact-list li {
    display: flex;
    align-items: center;
    gap: 10px;
    font-size: 12px;
    color: var(--ink);
    height: 22px;
  }
  .contact-list svg { width: 14px; height: 14px; flex: none; }
  .address {
    position: absolute;
    right: 40px;
    top: 232px;
    text-align: right;
    font-size: 12px;
    line-height: 22px;
    color: var(--ink);
  }
</style>
</head>
<body>
  <section class="card card-front">
    <span class="front-wordmark">VELLORIN</span>
  </section>

  <section class="card card-back">
    <span class="back-wordmark">VELLORIN</span>
    <div class="divider"></div>
    <div class="holder">
      <p class="holder-name">Daniel Marsh</p>
      <p class="holder-title">President</p>
    </div>
    <ul class="contact-list">
      <li>
        <svg viewBox="0 0 14 14"><rect x="3.5" y="1" width="7" height="12" rx="1.2" fill="none" stroke="#0f4a7e" stroke-width="1.3"/><circle cx="7" cy="11" r="0.7" fill="#0f4a7e"/></svg>
        412 308 5567
      </li>
      <li>
        <svg viewBox="0 0 14 14"><path d="M3 1.5 L5.5 1.5 L6.3 4.5 L4.8 5.6 C5.6 7.4 6.8 8.6 8.5 9.3 L9.6 7.8 L12.5 8.6 L12.5 11 C12.5 11.8 11.8 12.5 11 12.5 C6 12 2 8 1.5 3 C1.5 2.2 2.2 1.5 3 1.5 Z" fill="#0f4a7e"/></svg>
        415 220 9134
      </li>
      <li>
        <svg viewBox="0 0 14 14"><rect x="1" y="3" width="12" height="8.5" fill="#0f4a7e"/><path d="M1 3 L7 8 L13 3" fill="none" stroke="#f7f7f7" stroke-width="1"/></svg>
        info@vellorin.com
      </li>
      <li>
        <svg viewBox="0 0 14 14"><circle cx="7" cy="7" r="5.8" fill="none" stroke="#0f4a7e" stroke-width="1.2"/><ellipse cx="7" cy="7" rx="2.5" ry="5.8" fill="none" stroke="#0f4a7e" stroke-width="1"/><line x1="1.2" y1="7" x2="12.8" y2="7" stroke="#0f4a7e" stroke-width="1"/></svg>
        www.vellorin.com
      </li>
    </ul>
    <address class="address" style="font-style: normal;">
      Level 5, 27 Harbor Lane<br>
      Kestrel Bay, VIC 3100
    </address>
  </section>
</body>
</html>
```